Online Psychology Practice needs business cards.

Online Psychology service needs business cards. Have own logo- please see uploaded. I have other file formats if you need (not sure one needed?)

Details for Business Card:
Fiona Kettlewood
Clinical Psychologist BPsych, BPsych (Hons), MPsych (Clin), MAPS
T: 0457260714 | F: 08 71526804
E: hello@harbourlightmindcarestudio.com.au
W: harbourlightmindcarestudio.com.au

Industry/Entity Type

Health

Contact Information for Business Card

Logo plus details above (couldn't write in this section)

```html
<!DOCTYPE html>
<html lang="en">
<head>
<meta charset="utf-8">
<title>Harbourlight Mindcare Studio — Business Card</title>
<link href="https://fonts.googleapis.com/css2?family=Poppins:wght@400;500;600&display=swap" rel="stylesheet">
<style>
  :root {
    --backdrop: #c3c3c3;
    --paper: #ffffff;
    --navy: #1b5a82;
    --teal: #1a8ca8;
    --band-text: #ffffff;
  }
  * { margin: 0; padding: 0; box-sizing: border-box; }
  html, body { width: 1200px; height: 1000px; overflow: hidden; }
  body {
    background: var(--backdrop);
    font-family: "Poppins", sans-serif;
    position: relative;
  }
  .card {
    position: absolute;
    left: 226px;
    width: 747px;
    height: 427px;
    background: var(--paper);
    box-shadow: 0 3px 10px rgba(0,0,0,0.28);
    overflow: hidden;
  }
  .card--front { top: 53px; }
  .card--back { top: 520px; }

  .brand {
    position: absolute;
    display: flex;
    align-items: center;
    gap: 12px;
    color: var(--navy);
    font-weight: 500;
  }
  .brand__dot {
    flex: none;
    border-radius: 50%;
    background: var(--teal);
  }
  .brand__name { line-height: 1.15; }

  .card--front .brand {
    left: 0; right: 0; top: 170px;
    justify-content: center;
    font-size: 34px;
  }
  .card--front .brand__dot { width: 30px; height: 30px; }

  .card--back .brand {
    right: 50px; top: 120px;
    font-size: 20px;
  }
  .card--back .brand__dot { width: 18px; height: 18px; }

  .holder {
    position: absolute;
    left: 66px; top: 75px;
    color: var(--navy);
  }
  .holder__name {
    font-size: 28px;
    font-weight: 600;
    letter-spacing: -0.3px;
    text-transform: uppercase;
    line-height: 1;
  }
  .holder__title {
    margin-top: 12px;
    font-size: 14.5px;
    font-weight: 400;
    line-height: 18px;
  }

  .contact-band {
    position: absolute;
    left: 0; right: 0;
    top: 230px;
    height: 186px;
    background: var(--navy);
  }
  .contact-list {
    list-style: none;
    position: absolute;
    left: 68px; top: 24px;
    color: var(--band-text);
    font-size: 18px;
    font-weight: 400;
  }
  .contact-list li {
    display: flex;
    align-items: center;
    gap: 10px;
    height: 35px;
  }
  .contact-list svg { width: 19px; height: 19px; flex: none; fill: var(--band-text); }
</style>
</head>
<body>

<section class="card card--front">
  <div class="brand">
    <span class="brand__dot"></span>
    <span class="brand__name">Harbourlight Mindcare Studio</span>
  </div>
</section>

<section class="card card--back">
  <div class="holder">
    <h1 class="holder__name">Fiona Kettlewood</h1>
    <p class="holder__title">Clinical Psychologist BPsych,<br>BPsych (Hons), MPsych (Clin), MAPS</p>
  </div>

  <div class="brand">
    <span class="brand__dot"></span>
    <span class="brand__name">Harbourlight<br>Mindcare Studio</span>
  </div>

  <div class="contact-band">
    <ul class="contact-list">
      <li>
        <svg viewBox="0 0 20 20" aria-hidden="true"><path d="M1 7c0-3 4-4 9-4s9 1 9 4v2h-4V7H5v2H1z"/><path d="M4 10l2-2h8l2 2v7H4z"/><rect x="7" y="11" width="6" height="4" fill="#1b5a82"/></svg>
        <span>0457260714</span>
      </li>
      <li>
        <svg viewBox="0 0 20 20" aria-hidden="true"><rect x="5" y="1" width="10" height="5"/><rect x="1" y="7" width="18" height="8" rx="2"/><rect x="5" y="12" width="10" height="7" stroke="#1b5a82" stroke-width="1.5"/></svg>
        <span>08 71526804</span>
      </li>
      <li>
        <svg viewBox="0 0 20 20" aria-hidden="true"><circle cx="10" cy="10" r="8.5" fill="none" stroke="#fff" stroke-width="1.6"/><ellipse cx="10" cy="10" rx="3.5" ry="8.5" fill="none" stroke="#fff" stroke-width="1.4"/><path d="M2 7h16M2 13h16" stroke="#fff" stroke-width="1.4"/></svg>
        <span>harbourlightmindcarestudio.com.au</span>
      </li>
      <li>
        <svg viewBox="0 0 20 20" aria-hidden="true"><rect x="1" y="4" width="18" height="13"/><path d="M1 4l9 7 9-7M1 17l7-6M19 17l-7-6" fill="none" stroke="#1b5a82" stroke-width="1.3"/></svg>
        <span>hello@harbourlightmindcarestudio.com.au</span>
      </li>
    </ul>
  </div>
</section>

</body>
</html>
```